Health Supplement Series for 60 tablets of pure Gold Petal Grain powder

We need a packaging design theme for a health supplement for international consumers. Our initial product is called 'Gold Petal Grain'. It is for general health and is particularly effective for diabetic symptoms.
We would like to see designs that are clean and fresh.
It should give the impression of professional, premium pharmaceutical grade products.
Our company logo is attached below.

Target Market(s)

International

Industry/Entity Type

Health And Wellness

Font styles to use
Serif
Sans Serif

Requirements
Must have
• Bottle and box packaging required.
• 1st product is bottle of 60 tablets of 0.5gm each.
Should not have
• Seals and other "must buy" "guaranteed" etc

```html
<!DOCTYPE html>
<html lang="en">
<head>
<meta charset="utf-8">
<title>Natural Gold Petal Grain – Box Panels</title>
<link href="https://fonts.googleapis.com/css2?family=Anton&family=Oswald:wght@300;400;600&display=swap" rel="stylesheet">
<style>
  :root{
    --page:#e4e4e4;
    --paper:#f8efec;
    --ink:#3b3b3b;
    --green:#4e9a34;
    --green-dark:#2f6b22;
    --seed:#7a4a2a;
    --seed-light:#b07a50;
  }
  *{box-sizing:border-box;margin:0;padding:0}
  html,body{width:1200px;height:1091px;overflow:hidden;background:var(--page)}
  .canvas{position:relative;width:1200px;height:1091px}
  .panel{position:absolute;top:105px;height:880px;background:var(--paper);overflow:hidden}
  .panel--side{left:180px;width:280px;border-right:1px solid #e3d8d4}
  .panel--front{left:460px;width:560px}

  .brand{display:flex;align-items:center;gap:7px;font-family:"Oswald",sans-serif;font-weight:600;color:var(--green);text-transform:uppercase;letter-spacing:.5px;line-height:1}
  .brand__mark{width:18px;height:18px;background:var(--green);flex:none}

  /* front */
  .band{position:absolute;left:347px;top:0;width:46px;height:225px;background:linear-gradient(160deg,#3f8a2d,#8cc56a 35%,#2f6b22 60%,#7dbb5a 85%,#46902f)}
  .panel--front .brand{position:absolute;left:0;right:0;top:248px;justify-content:center;font-size:20px}
  .title{position:absolute;left:0;right:0;top:300px;text-align:center;font-family:"Anton",sans-serif;color:var(--ink);font-size:70px;line-height:1.02;letter-spacing:1px;text-transform:uppercase}
  .seed{position:absolute;border-radius:50%;background:radial-gradient(circle at 40% 35%,var(--seed-light),var(--seed) 70%)}
  .panel--front .seed{left:244px;top:486px;width:72px;height:60px}
  .arc{position:absolute}
  .panel--front .arc{left:130px;top:470px;width:300px;height:150px}
  .count{position:absolute;left:50%;top:655px;transform:translateX(-50%);background:var(--ink);color:#fff;font-family:"Oswald",sans-serif;font-weight:300;font-size:30px;padding:4px 16px;line-height:1.2}

  /* side */
  .side-title{position:absolute;left:0;right:0;top:55px;text-align:center;font-family:"Anton",sans-serif;color:var(--ink);font-size:27px;line-height:1.05;text-transform:uppercase}
  .panel--side .seed{left:122px;top:142px;width:34px;height:30px}
  .panel--side .arc{left:70px;top:130px;width:140px;height:70px}
  .facts{position:absolute;left:20px;top:235px;width:240px;border:6px solid var(--green);background:#fff;padding:8px 8px 10px;font-family:"Oswald",sans-serif;color:#222;font-size:10.5px;line-height:1.45}
  .facts__head{font-size:27px;font-weight:600;line-height:1;border-bottom:1px solid #222;padding-bottom:3px}
  .facts__serving{font-size:10px;border-bottom:6px solid #222;padding:2px 0 3px}
  .row{display:flex;justify-content:space-between;border-bottom:1px solid #555}
  .row--thick{border-bottom-width:4px}
  .row--indent{padding-left:10px}
  .b{font-weight:600}
  .facts__note{font-size:8.5px;line-height:1.35;margin-top:5px;border-top:4px solid #222;padding-top:4px}
  .grid{display:grid;grid-template-columns:1.6fr 1fr 1fr 1fr;font-size:8.5px;line-height:1.35;margin-top:4px}
  .panel--side .brand{position:absolute;right:20px;bottom:45px;font-size:16px}
</style>
</head>
<body>
<div class="canvas">

  <section class="panel panel--side">
    <h2 class="side-title">Natural<br>Gold Petal<br>Grain</h2>
    <div class="seed" role="img" aria-label="Illustration of cracked seed pods"></div>
    <svg class="arc" viewBox="0 0 140 70" aria-hidden="true">
      <path id="arcSide" d="M18 30 A52 40 0 0 0 122 30" fill="none"/>
      <text font-family="Oswald,sans-serif" font-size="8" fill="#3b3b3b" letter-spacing="1"><textPath href="#arcSide" startOffset="50%" text-anchor="middle">• GRAIN SEED TABLETS •</textPath></text>
    </svg>

    <div class="facts">
      <div class="facts__head">Nutrition Facts</div>
      <div class="facts__serving">Serving Size 4 Pieces</div>
      <div class="row"><span class="b">Amount Per Serving</span></div>
      <div class="row row--thick"><span><span class="b">Calories</span> 110</span></div>
      <div class="row"><span></span><span class="b">% Daily Value*</span></div>
      <div class="row"><span><span class="b">Total Fat</span> 2.5g</span><span class="b">4%</span></div>
      <div class="row row--indent"><span>Saturated Fat 1g</span><span class="b">5%</span></div>
      <div class="row row--indent"><span>Trans Fat 0g</span><span></span></div>
      <div class="row"><span><span class="b">Cholesterol</span> 0mg</span><span class="b">0%</span></div>
      <div class="row"><span><span class="b">Sodium</span> 170mg</span><span class="b">7%</span></div>
      <div class="row"><span><span class="b">Total Carbohydrate</span> 21g</span><span class="b">7%</span></div>
      <div class="row row--indent"><span>Dietary Fiber 0g</span><span class="b">0%</span></div>
      <div class="row row--indent"><span>Sugars 13g</span><span></span></div>
      <div class="row row--thick"><span><span class="b">Protein</span> 0g</span><span class="b">0%</span></div>
      <p class="facts__note">*Percent Daily Values are based on a 2,000 calorie diet. Your Daily Values may be higher or lower depending on your calorie needs.</p>
      <div class="grid">
        <span></span><span>Calories</span><span>2,000</span><span>2,500</span>
        <span>Total Fat</span><span>Less than</span><span>65g</span><span>80g</span>
        <span>Sat Fat</span><span>Less than</span><span>20g</span><span>25g</span>
        <span>Cholesterol</span><span>Less than</span><span>300mg</span><span>300mg</span>
        <span>Sodium</span><span>Less than</span><span>2400mg</span><span>2400mg</span>
        <span>Total Carbohydrate</span><span></span><span>300g</span><span>375g</span>
        <span>Dietary Fiber</span><span></span><span>25g</span><span>30g</span>
      </div>
    </div>

    <div class="brand"><span class="brand__mark"></span>Norvale Life Sciences</div>
  </section>

  <section class="panel panel--front">
    <div class="band" role="img" aria-label="Green marbled decorative band"></div>
    <div class="brand"><span class="brand__mark"></span>Norvale Life Sciences</div>
    <h1 class="title">Natural Gold<br>Petal Grain</h1>
    <div class="seed" role="img" aria-label="Illustration of cracked seed pods"></div>
    <svg class="arc" viewBox="0 0 300 150" aria-hidden="true">
      <path id="arcFront" d="M30 70 A120 80 0 0 0 270 70" fill="none"/>
      <text font-family="Oswald,sans-serif" font-weight="300" font-size="22" fill="#3b3b3b" letter-spacing="1"><textPath href="#arcFront" startOffset="50%" text-anchor="middle">• GRAIN SEED TABLETS •</textPath></text>
    </svg>
    <div class="count">60 tablets</div>
  </section>

</div>
</body>
</html>
```